Collectibles expert needs a new business card design.

My current business card makes me look to high end. It may even make me look arrogant or too stuffy. I do work with high end clients and their items but most of my business is with average people with average items. My business name is Walter Brumby's Old Mill Digging Co. The idea was that I mine the streets helping people discover the treasures buried in their homes. That could be art, jewelry, coins, etc. The name and an older logo I used does not make immediate sense to most people. I tried to go with just my picture and name and that is the current card I am changing. I help people who need to downsize. Whether they are getting rid of one item, a collection or a house full of items I help them discover what they have, what it is worth and what are the best ways we can get the most for them. This may be a combination of estate sale (which I dont do) auction or sell directly to a dealer or collector. Usually it is a combination of these. My main goal is to help make sure they dont accidently sell a Vandermeer painting in a garage sale. I am uploading a copy of my old card and the old logo I used to use but the winning card design will need to be much different than these. You can learn a little more about me at www.walterkbrumby.example, www.oldmilldigng.example and www.facebook.com/omdco. I hope someone can look at what I do and come up with a very unique design that will be equally effective if my client is high income or if my client is low to mid income. I do not care if it is a one or two sided card as long as it conveys my contact information and a good representation of what I do.

Target Market(s)

People who are getting rid of items. These can be elderly couples or individuals that are moving to an active living community and will have less space so they need to sell items. This can also include the children of elder parents that dont want their stuff and want to find solutions to help them get rid of their items.

Contact Information for Business Card

The card should have my business name Walter Brumby's Old Mill Digging Co., phone number 555-312-70981, email walter@oldmilldigging.example and website www.oldmilldigging.example. Would also like to include Buyer, Broker, Consultant and Appraiser. We can put Walter K. Brumby, ISA on the opposite side of the company name since it includes my name as well.

Font styles to use
Sans Serif

Colors

Designer to choose colors to be used in the design.

Requirements
Must have
• My project must have a professional look. It must not alienate low income clients and should still be appealing to high value clients.

```html
<!DOCTYPE html>
<html lang="en">
<head>
<meta charset="utf-8">
<title>Old Mill Digging Co. — Business Card</title>
<link rel="stylesheet" href="https://fonts.googleapis.com/css2?family=Bebas+Neue&family=Lato:wght@400;700&family=Oswald:wght@600&display=swap">
<style>
  :root {
    --backdrop: #3a3a3a;
    --gold: #9e7433;
    --paper: #f6f6f6;
    --ink: #2b2622;
    --mark-grey: #5b5b5d;
    --on-gold: #ffffff;
    --rule: rgba(255,255,255,0.55);
  }
  * { margin: 0; padding: 0; box-sizing: border-box; }
  html, body {
    width: 1200px; height: 900px; overflow: hidden;
    background: var(--backdrop);
  }
  .canvas { position: relative; width: 1200px; height: 900px; }

  .card {
    position: absolute;
    width: 477px; height: 294px;
    box-shadow: 3px 4px 6px rgba(0,0,0,0.45);
  }
  .card--contact {
    left: 120px; top: 275px;
    background: var(--gold);
    border-radius: 0 52px 0 52px;
    color: var(--on-gold);
    text-align: center;
  }
  .card--brand {
    left: 606px; top: 274px; height: 292px;
    background: var(--paper);
    border-radius: 56px 0 56px 0;
    text-align: center;
  }

  .holder-name {
    position: absolute; left: 0; right: 0; top: 89px;
    font-family: "Bebas Neue", sans-serif;
    font-size: 22px; letter-spacing: 0.5px; line-height: 1;
  }
  .holder-role {
    position: absolute; left: 0; right: 0; top: 109px;
    font-family: "Lato", sans-serif; font-size: 14px;
  }
  .divider {
    position: absolute; left: 168px; width: 141px; top: 140px;
    height: 1px; background: var(--rule);
  }
  .contact-list {
    position: absolute; left: 0; right: 0; top: 153px;
    list-style: none;
    font-family: "Lato", sans-serif; font-size: 13.5px; line-height: 17px;
  }
  .contact-list b { font-weight: 700; }

  .brand-square {
    position: absolute; left: 208px; top: 76px;
    width: 62px; height: 62px;
  }
  .brand-name {
    position: absolute; left: 0; right: 0; top: 174px;
    font-family: "Oswald", sans-serif; font-weight: 600;
    font-size: 22px; line-height: 26px;
    color: var(--ink); text-transform: uppercase;
  }
</style>
</head>
<body>
<main class="canvas">
  <section class="card card--contact">
    <h1 class="holder-name">Walter K. Brumby, ISA</h1>
    <p class="holder-role">Buyer, Broker, Consultant and Appraiser</p>
    <div class="divider"></div>
    <ul class="contact-list">
      <li><b>P:</b> 555-312-70981</li>
      <li><b>E:</b> walter@oldmilldigging.example</li>
      <li>www.oldmilldigging.example</li>
    </ul>
  </section>

  <section class="card card--brand">
    <svg class="brand-square" viewBox="0 0 62 62" aria-hidden="true">
      <rect width="62" height="62" fill="var(--mark-grey)"/>
    </svg>
    <h2 class="brand-name">Walter Brumby's<br>Old Mill Digging Co.</h2>
  </section>
</main>
</body>
</html>
```